KPV Construction we build lodges in Botswana

We need a Design Layout only with Categories where we can update each projects photos.... We have a web address and a host - kpv.construction

```html
<!DOCTYPE html>
<html lang="en">
<head>
<meta charset="utf-8">
<title>KPV Construction</title>
<link href="https://fonts.googleapis.com/css2?family=Michroma&family=Lato:wght@400;700&display=swap" rel="stylesheet">
<style>
:root{
  --blue:#1b63b5;
  --blue-dark:#1457a3;
  --red:#ef4646;
  --ink:#1d1d1d;
  --text:#555;
  --muted:#777;
  --line:#e3e3e3;
  --footer:#232323;
  --white:#fff;
}
*{box-sizing:border-box;margin:0;padding:0}
html,body{width:1200px;height:3442px;overflow:hidden}
body{position:relative;background:var(--white);font-family:'Lato',sans-serif;color:var(--text)}
.abs{position:absolute}
.display{font-family:'Michroma',sans-serif;color:var(--ink);text-transform:uppercase}
.btn{position:absolute;display:flex;align-items:center;justify-content:center;background:var(--blue);color:var(--white);font:700 14px 'Lato',sans-serif;border-radius:2px}
.btn.red{background:var(--red)}

/* header */
.site-header{position:absolute;left:0;top:0;width:1200px;height:131px}
.menu-toggle{left:120px;top:48px}
.brand{position:absolute;display:flex;align-items:center;gap:10px;font:700 22px 'Lato',sans-serif;color:var(--blue);letter-spacing:.5px}
.brand-mark{width:14px;height:14px;background:var(--red)}
.site-header .brand{left:500px;top:48px}
.contact-btn{left:940px;top:50px;width:138px;height:34px}

/* hero */
.hero{position:absolute;left:0;top:131px;width:1200px;height:619px;overflow:hidden}
.hero-photo{position:absolute;inset:0;background:
  radial-gradient(ellipse at 55% 45%,#6b5038 0%,#3f3222 40%,transparent 70%),
  linear-gradient(180deg,#6f7c4a 0%,#3a3a24 45%,#4b5a2e 75%,#7a6d56 100%)}
.hero-shade{position:absolute;inset:0;background:rgba(0,0,0,.25)}
.hero-diamond{left:440px;top:180px}
.hero-title{position:absolute;left:0;width:1200px;top:226px;text-align:center;font:400 30px/38px 'Michroma',sans-serif;color:var(--white);letter-spacing:1px}
.hero-title span{display:block}
.hero-title .underline{width:130px;height:2px;background:var(--white);margin:0 auto}
.hero-text{position:absolute;left:370px;width:460px;top:326px;text-align:center;font:700 14px/19px 'Lato',sans-serif;color:var(--white)}
.hero .btn{top:387px;height:33px;width:137px;font-size:13px}
.hero .read{left:450px}
.hero .start{left:606px}
.hero-dots{position:absolute;left:580px;top:563px;display:flex;gap:5px}
.hero-dots i{width:7px;height:7px;border-radius:50%;background:rgba(255,255,255,.6)}
.hero-dots i.on{background:var(--white)}
.hero-arrow{top:300px}

/* features */
.feature{position:absolute;top:837px;height:161px;display:flex;gap:14px;padding:38px 14px}
.feature.active{border:1px solid #d6d6d6;box-shadow:0 2px 6px rgba(0,0,0,.06)}
.feature h3{font:400 13px 'Michroma',sans-serif;color:var(--ink);text-transform:uppercase;margin-top:2px}
.feature h3::after{content:"";display:block;width:60px;height:3px;background:var(--blue);margin:6px 0 8px}
.feature p{font:400 13px/17px 'Lato',sans-serif;color:var(--text)}

/* section titles */
.section-title{position:absolute;left:0;width:1200px;text-align:center}

/* services */
.service-bars{left:214px;top:1163px}
.service-photo{position:absolute;left:229px;top:1163px;width:452px;height:335px;background:
  radial-gradient(ellipse at 40% 60%,#4a3429 0%,#5b4a44 35%,transparent 65%),
  linear-gradient(180deg,#cfd1d4 0%,#9a9ca0 45%,#6e6a68 100%)}
.play{left:420px;top:1310px}
.service-copy{position:absolute;left:716px;top:1160px;width:376px}
.service-copy h3{font:400 18px 'Michroma',sans-serif;color:var(--ink);margin-bottom:16px;text-transform:uppercase}
.service-copy p{font:400 13px/18px 'Lato',sans-serif;color:var(--text);margin-bottom:14px}
.service-copy ul{list-style:none;margin-top:20px}
.service-copy li{font:700 13px/25px 'Lato',sans-serif;color:var(--ink);padding-left:22px;position:relative}
.service-copy li::before{content:"";position:absolute;left:0;top:10px;width:6px;height:6px;border-radius:50%;background:var(--blue)}
.service-btn{left:716px;top:1464px;width:137px;height:34px}

/* projects */
.project{position:absolute;width:310px;height:268px}
.project.overlay{background:linear-gradient(180deg,#1d1a18,#2c2622)}
.project-name{position:absolute;left:24px;top:16px;font:700 15px 'Lato',sans-serif;color:var(--white)}
.project-name small{display:block;font:400 11px 'Lato',sans-serif;color:#ddd;margin-top:2px}
.expand{left:137px;top:119px}
.projects-btn{left:530px;top:2278px;width:140px;height:34px}

/* newsletter */
.news-form{position:absolute;left:268px;top:2418px;width:650px;height:53px;border:1px solid #cfcfcf;display:flex}
.news-form span{flex:1;padding:0 24px;font:400 13px/51px 'Lato',sans-serif;color:#aaa}
.news-send{width:81px;background:var(--blue);display:flex;align-items:center;justify-content:center}
.news-note{position:absolute;left:0;width:1200px;top:2505px;text-align:center;font:400 14px 'Lato',sans-serif;color:var(--text)}

/* blogs */
.blog{position:absolute;top:2608px;width:316px;height:333px;background:#f7f7f7;padding:14px}
.blog-photo{height:181px;position:relative}
.date{position:absolute;left:0;top:18px;width:34px;height:38px;background:var(--red);color:var(--white);text-align:center;font:700 12px/13px 'Lato',sans-serif;padding-top:5px}
.date small{display:block;font-size:10px}
.blog h4{font:400 12px 'Michroma',sans-serif;color:var(--ink);margin:14px 0 6px;letter-spacing:.5px}
.meta{display:flex;align-items:center;font:400 13px 'Lato',sans-serif;color:var(--ink);gap:6px;margin-bottom:10px}
.meta .grow{flex:1}
.blog p{font:400 13px/18px 'Lato',sans-serif;color:var(--text)}
.blog .more{font:400 13px 'Lato',sans-serif;color:var(--text);margin-top:4px}
.blogs-btn{left:523px;top:2975px;width:154px;height:35px;font-size:16px}

/* footer */
.site-footer{position:absolute;left:0;top:3056px;width:1200px;height:325px;background:var(--footer);color:var(--white)}
.foot-col{position:absolute;top:84px}
.foot-col h5{font:400 13px 'Michroma',sans-serif;color:var(--white);text-transform:uppercase}
.foot-col h5::after{content:"";display:block;width:32px;height:2px;background:var(--blue);margin:6px 0 18px}
.foot-col p{font:400 13px/19px 'Lato',sans-serif;color:var(--white)}
.foot-input{margin-top:24px;width:186px;height:34px;background:var(--white);display:flex;border-radius:2px;overflow:hidden}
.foot-input span{flex:1;font:400 11px/34px 'Lato',sans-serif;color:#444;padding-left:16px}
.foot-input b{width:36px;background:var(--red);display:flex;align-items:center;justify-content:center}
.links{list-style:none}
.links li{font:400 13px/23px 'Lato',sans-serif;padding-left:20px;position:relative}
.links li::before{content:"";position:absolute;left:2px;top:9px;width:5px;height:5px;border-right:1.5px solid #fff;border-top:1.5px solid #fff;transform:rotate(45deg)}
.office li{list-style:none;font:400 13px/20px 'Lato',sans-serif;position:relative;padding-left:38px;margin-bottom:4px}
.office svg{position:absolute;left:0;top:3px}
.site-footer .brand{color:var(--white);font-size:18px}
.bottom-bar{position:absolute;left:0;top:3381px;width:1200px;height:61px;background:var(--blue)}
.bottom-bar p{position:absolute;left:119px;top:22px;font:700 13px 'Lato',sans-serif;color:var(--white)}
.socials{position:absolute;left:895px;top:20px;display:flex;gap:12px}
.socials i{width:22px;height:22px;border-radius:50%;background:var(--red);display:block}
.socials i+i{background:var(--white);opacity:.9}
</style>
</head>
<body>

<header class="site-header">
  <svg class="abs menu-toggle" width="26" height="22" viewBox="0 0 26 22" aria-hidden="true"><g fill="#1d1d1d"><rect x="0" y="2" width="18" height="3"/><rect x="0" y="9" width="18" height="3"/><rect x="0" y="16" width="18" height="3"/><circle cx="23" cy="3.5" r="1.6"/><circle cx="23" cy="10.5" r="1.6"/><circle cx="23" cy="17.5" r="1.6"/></g></svg>
  <div class="brand"><span class="brand-mark"></span>KPV Construction</div>
  <a class="btn contact-btn">Contact us</a>
</header>

<section class="hero">
  <div class="hero-photo" role="img" aria-label="Timber log lodge among forest trees"></div>
  <div class="hero-shade"></div>
  <svg class="abs hero-diamond" width="320" height="260" viewBox="0 0 320 260" aria-hidden="true"><path d="M160 4 L316 130 L160 256 L4 130 Z" fill="rgba(255,255,255,.06)" stroke="rgba(255,255,255,.25)" stroke-width="1.5"/></svg>
  <h1 class="hero-title"><span>Construction</span><span>Company</span><span class="underline"></span></h1>
  <p class="hero-text">We are a Construction Company basedin the Okavango Delta and specialize in Lodge building...</p>
  <a class="btn read">Read More</a>
  <a class="btn red start">Get Started</a>
  <div class="hero-dots"><i></i><i class="on"></i><i></i><i></i></div>
  <svg class="abs hero-arrow" style="left:26px" width="12" height="18" viewBox="0 0 12 18" aria-hidden="true"><path d="M10 2 L3 9 L10 16" fill="none" stroke="#fff" stroke-width="3"/></svg>
  <svg class="abs hero-arrow" style="left:1162px" width="12" height="18" viewBox="0 0 12 18" aria-hidden="true"><path d="M2 2 L9 9 L2 16" fill="none" stroke="#fff" stroke-width="3"/></svg>
</section>

<section class="features">
  <div class="feature" style="left:119px;width:300px">
    <svg width="46" height="52" viewBox="0 0 46 52" aria-hidden="true"><g fill="none" stroke="#1b63b5" stroke-width="2"><path d="M23 10 a12 12 0 0 1 7 21 v6 h-14 v-6 a12 12 0 0 1 7 -21z"/><path d="M17 41 h12 M19 45 h8"/><path d="M23 2 v4 M8 8 l3 3 M38 8 l-3 3 M2 22 h4 M40 22 h4"/></g></svg>
    <div><h3>Creative &amp; Innovation</h3><p>Lorem Ipsum is simply dummy<br>text of the printing typesetting<br>in the industry.</p></div>
  </div>
  <div class="feature active" style="left:438px;width:314px">
    <svg width="54" height="52" viewBox="0 0 54 52" aria-hidden="true"><g fill="none" stroke="#1b63b5" stroke-width="2"><path d="M3 24 L27 6 L51 24"/><path d="M9 20 v26 h36 v-26"/><path d="M9 28 h36 M9 36 h36"/><rect x="22" y="30" width="10" height="16"/></g></svg>
    <div><h3>Build Lodges</h3><p>Lorem Ipsum is simply dummy<br>text of the printing typesetting<br>in the industry.</p></div>
  </div>
  <div class="feature" style="left:785px;width:300px">
    <svg width="46" height="52" viewBox="0 0 46 52" aria-hidden="true"><g fill="none" stroke="#1b63b5" stroke-width="2"><path d="M23 3 l5 6 7-2 1 7 7 3-3 7 3 7-7 3-1 7-7-2-5 6-5-6-7 2-1-7-7-3 3-7-3-7 7-3 1-7 7 2z"/><path d="M16 26 l5 5 9-10"/></g></svg>
    <div><h3>Satisfaction</h3><p>Lorem Ipsum is simply dummy<br>text of the printing typesetting<br>in the industry.</p></div>
  </div>
</section>

<h2 class="section-title display" style="top:1066px;font-size:34px">Our Services</h2>

<section class="services">
  <svg class="abs service-bars" width="6" height="330" viewBox="0 0 6 330" aria-hidden="true"><rect x="0" y="0" width="5" height="70" fill="#ef4646"/><rect x="0" y="90" width="5" height="70" fill="#1b63b5"/><rect x="0" y="180" width="5" height="70" fill="#1b63b5"/><rect x="0" y="270" width="5" height="60" fill="#1b63b5"/></svg>
  <div class="service-photo" role="img" aria-label="Wooden lodge with steep roofs in misty forest"></div>
  <svg class="abs play" width="40" height="40" viewBox="0 0 40 40" aria-hidden="true"><circle cx="20" cy="20" r="17" fill="none" stroke="#ef4646" stroke-width="3"/><path d="M16 12 L28 20 L16 28 Z" fill="#ef4646"/></svg>
  <div class="service-copy">
    <h3>Build Lodges</h3>
    <p>Lorem Ipsum is simply dummy text of the printing and typesetting industry. Lorem Ipsum has been the industry standard dummy text ever since the 1500s,</p>
    <p>when an unknown printer took a galley of type and scrambled it to make a type specimen book. It has survived not only five centuries,</p>
    <ul><li>Lorem Ipsum is simply dummy.</li><li>Lorem Ipsum is simply dummy.</li><li>Lorem Ipsum is simply dummy.</li></ul>
  </div>
  <a class="btn service-btn">Read More</a>
</section>

<h2 class="section-title display" style="top:1588px;font-size:25px">Recently Projects</h2>

<section class="projects">
  <div class="project" style="left:119px;top:1684px;background:linear-gradient(180deg,#9fb7c8 0%,#6f7a5a 40%,#6a3b25 70%,#8a8a5a 100%)" role="img" aria-label="Red timber lodge on a green hillside"></div>
  <div class="project overlay" style="left:445px;top:1684px" role="img" aria-label="Lodge under construction, timber frame">
    <div class="project-name">Project Name<small>Country,City</small></div>
    <svg class="abs expand" width="36" height="32" viewBox="0 0 36 32" aria-hidden="true"><g fill="none" stroke="#fff" stroke-width="2.5"><path d="M2 10 V2 H10 M26 2 H34 V10 M34 22 V30 H26 M10 30 H2 V22"/></g></svg>
  </div>
  <div class="project" style="left:771px;top:1684px;background:linear-gradient(180deg,#7fa8d8 0%,#c9d8e6 35%,#9a5a3a 60%,#7d9a4c 100%)" role="img" aria-label="Timber lodge with wide deck and steps"></div>
  <div class="project" style="left:119px;top:1968px;background:linear-gradient(180deg,#d9e4ec 0%,#8a6a4a 45%,#b89a7a 75%,#c8c0b0 100%)" role="img" aria-label="Modern timber lodge with covered terrace"></div>
  <div class="project" style="left:445px;top:1968px;background:linear-gradient(180deg,#4d6a3a 0%,#7a4a30 45%,#5a3a28 65%,#5c9a3a 100%)" role="img" aria-label="Dark timber cabin with picnic table on lawn"></div>
  <div class="project" style="left:771px;top:1968px;background:linear-gradient(180deg,#8fb0d6 0%,#3c4048 40%,#c9a46a 65%,#7aa04a 100%)" role="img" aria-label="Flat-roof timber lodge with glazed front and deck"></div>
  <a class="btn projects-btn">View More</a>
</section>

<h2 class="section-title display" style="top:2359px;font-size:25px">Subscribe for Newsletter</h2>
<div class="news-form"><span>Your E-Mail</span>
  <div class="news-send"><svg width="30" height="28" viewBox="0 0 30 28" aria-hidden="true"><path d="M2 13 L28 2 L22 26 L14 18 L24 6 L11 16 Z" fill="#fff"/></svg></div>
</div>
<p class="news-note">Keep Up to Date with our work and Projects</p>

<h2 class="section-title display" style="top:2552px;font-size:36px">Blogs</h2>

<section class="blogs">
  <article class="blog" style="left:108px">
    <div class="blog-photo" role="img" aria-label="Lodge interior with dining table and open doors" style="background:linear-gradient(180deg,#c8a27a 0%,#8fb46a 45%,#9a6a4a 70%,#6a4a30 100%)"><div class="date">20<small>Jan</small></div></div>
    <h4>BLOG TITLE HEADING</h4>
    <div class="meta"><svg width="12" height="12" viewBox="0 0 12 12" aria-hidden="true"><rect x="1" y="2" width="10" height="9" fill="none" stroke="#333" stroke-width="1.3"/><path d="M1 5 h10" stroke="#333"/></svg><span class="grow">&nbsp;Jan 21, 2019</span><span>♡20</span><span>&nbsp;♡12</span></div>
    <p>Lorem Ipsum is simply dummy text of the matter and typesetting in industry.</p>
    <p class="more">Read More ⊕</p>
  </article>
  <article class="blog" style="left:443px">
    <div class="blog-photo" role="img" aria-label="Thatched lodge deck at sunset" style="background:linear-gradient(180deg,#e8a860 0%,#b87040 40%,#6a3a22 70%,#3a2418 100%)"><div class="date">21<small>Jan</small></div></div>
    <h4>BLOG TITLE HEADING</h4>
    <div class="meta"><svg width="12" height="12" viewBox="0 0 12 12" aria-hidden="true"><rect x="1" y="2" width="10" height="9" fill="none" stroke="#333" stroke-width="1.3"/><path d="M1 5 h10" stroke="#333"/></svg><span class="grow">&nbsp;Jan 22, 2019</span><span>♡20</span><span>&nbsp;♡12</span></div>
    <p>Lorem Ipsum is simply dummy text of the matter and typesetting in industry.</p>
    <p class="more">Read More ⊕</p>
  </article>
  <article class="blog" style="left:778px">
    <div class="blog-photo" role="img" aria-label="Thatched lodge lit at dusk" style="background:linear-gradient(180deg,#20242e 0%,#4a3a2a 40%,#c08040 65%,#2a2018 100%)"><div class="date">21<small>Jan</small></div></div>
    <h4>BLOG TITLE HEADING</h4>
    <div class="meta"><svg width="12" height="12" viewBox="0 0 12 12" aria-hidden="true"><rect x="1" y="2" width="10" height="9" fill="none" stroke="#333" stroke-width="1.3"/><path d="M1 5 h10" stroke="#333"/></svg><span class="grow">&nbsp;April10, 2018</span><span>♡20</span><span>&nbsp;♡12</span></div>
    <p>Lorem Ipsum is simply dummy text of the matter and typesetting in industry.</p>
    <p class="more">Read More ⊕</p>
  </article>
  <a class="btn blogs-btn">View More</a>
</section>

<footer class="site-footer">
  <div class="foot-col" style="left:119px;width:230px">
    <h5>Subscribe</h5>
    <p>Get the latest updates and offer Lorem Ipsum is simply dummy text of the printing.</p>
    <div class="foot-input"><span>Enter Your Email</span><b><svg width="16" height="12" viewBox="0 0 16 12" aria-hidden="true"><rect x="1" y="1" width="14" height="10" fill="none" stroke="#fff" stroke-width="1.5"/><path d="M1 1 L8 7 L15 1" fill="none" stroke="#fff" stroke-width="1.5"/></svg></b></div>
  </div>
  <div class="foot-col" style="left:404px">
    <h5>Quick Links</h5>
    <ul class="links"><li>Home</li><li>About us</li><li>Services</li><li>Blogs</li><li>Testimonials</li><li>Contact us</li></ul>
  </div>
  <div class="foot-col office" style="left:594px;width:240px">
    <h5 style="margin-left:38px">Office</h5>
    <ul>
      <li><svg width="14" height="16" viewBox="0 0 14 16" aria-hidden="true"><path d="M7 1 a5 5 0 0 1 5 5 c0 4-5 9-5 9 s-5-5-5-9 a5 5 0 0 1 5-5z" fill="#fff"/><circle cx="7" cy="6" r="2" fill="#232323"/></svg>Delta Lodge Office<br>18 Riverside Road West<br>Maun, Botswana 0000</li>
      <li><svg width="14" height="14" viewBox="0 0 14 14" aria-hidden="true"><path d="M3 1 l3 3-2 2 c1 2 2 3 4 4 l2-2 3 3-2 2 C6 13 1 8 1 3z" fill="#fff"/></svg>+267 555 0143</li>
      <li><svg width="14" height="12" viewBox="0 0 14 12" aria-hidden="true"><rect x="1" y="1" width="12" height="10" fill="#fff"/><path d="M1 1 L7 6 L13 1" fill="none" stroke="#232323"/></svg>info@kpv.construction</li>
      <li><svg width="14" height="14" viewBox="0 0 14 14" aria-hidden="true"><circle cx="7" cy="7" r="6" fill="#fff"/><path d="M7 3 v4 h3" stroke="#232323" stroke-width="1.5" fill="none"/></svg>Mon-Sat 9:00am-6 :00pm</li>
    </ul>
  </div>
  <div class="foot-col" style="left:863px;width:230px;top:70px">
    <div class="brand" style="position:static;margin-bottom:28px"><span class="brand-mark"></span>KPV Construction</div>
    <p>Lorem Ipsum is simply dummy text the printing and typesetting industry. Lorem Ipsum hasbeen the industry standard.</p>
    <p style="margin-top:16px">Read More ⊕</p>
  </div>
</footer>

<div class="bottom-bar">
  <p>© Copyright 2019 Construction. All Rights Reserved</p>
  <div class="socials"><i></i><i></i><i></i><i></i><i></i></div>
</div>

</body>
</html>
```